Tamsel Foundation Letterhead

We are a newly established non profit registered in Maryland but operates in Africa, south of the sahara. We offer scholarships to deserving young adults from high school through college. Our color theme for our existing logo is purple, we want a design that is stylish, spellbinding yet a letterhead that projects seriousness. More information on www.thetamselfoundation.example

Target Market(s)

High school and college students in sub saharan African as well as our donors in the US

Industry/Entity Type

Non Profit

Font styles to use
Script

Requirements
Must have
• Logo at the top and if possible watermark the logo in the middle of the letterhead, contact address,
Should not have
• NA

```html
<!DOCTYPE html>
<html lang="en">
<head>
<meta charset="utf-8">
<title>Tamsel Foundation Letterhead</title>
<link href="https://fonts.googleapis.com/css2?family=Marcellus+SC&family=Lato:wght@400;700&display=swap" rel="stylesheet">
<style>
  :root {
    --backdrop: #ffffff;
    --paper: #ffffff;
    --brand-purple: #6a3a9a;
    --brand-deep: #5b2d8e;
    --brand-plum: #7b4a8c;
    --ring-grey: #ececf1;
    --mark-grey: #cfcbdb;
    --watermark-lilac: #ddd3ea;
    --contact-ink: #5b2d8e;
    --band-text: #ffffff;
  }
  * { margin: 0; padding: 0; box-sizing: border-box; }
  html, body {
    width: 1200px; height: 1000px; overflow: hidden;
    background: var(--backdrop);
  }
  .letterhead {
    position: absolute; left: 262px; top: 79px;
    width: 649px; height: 841px;
    background: var(--paper);
    box-shadow: 0 0 0 1px #eeeeee;
    overflow: hidden;
  }
  .masthead {
    position: absolute; left: 146px; top: 28px;
    display: flex; align-items: center; gap: 14px;
  }
  .masthead-badge {
    width: 62px; height: 62px; border-radius: 50%;
    border: 4px solid var(--mark-grey);
  }
  .masthead-text { width: 280px; color: var(--brand-purple); }
  .masthead-the {
    display: flex; align-items: center; gap: 8px;
    font-family: "Marcellus SC", serif; font-size: 8px; letter-spacing: 2px;
  }
  .masthead-the::before, .masthead-the::after {
    content: ""; flex: 1; height: 1px; background: var(--brand-purple);
  }
  .masthead-name {
    font-family: "Marcellus SC", serif; font-size: 24px; letter-spacing: 0.3px;
    line-height: 1; white-space: nowrap; text-align: center;
    border-bottom: 1px solid var(--brand-purple);
    padding: 1px 0 5px;
  }
  .masthead-tagline {
    font-family: "Lato", sans-serif; font-size: 6.4px; letter-spacing: 2.2px;
    text-transform: uppercase; margin-top: 3px; white-space: nowrap;
    border-bottom: 1px solid var(--brand-purple); padding-bottom: 3px;
  }
  .watermark {
    position: absolute; left: 212px; top: 334px;
    width: 218px; height: 218px; border-radius: 50%;
    border: 11px solid var(--ring-grey);
    display: flex; align-items: center; justify-content: center;
  }
  .watermark-name {
    font-family: "Marcellus SC", serif; font-size: 24px; line-height: 1.15;
    color: var(--watermark-lilac); text-align: center;
  }
  .contact-row {
    position: absolute; left: 0; right: 0; top: 786px;
    display: flex; justify-content: center; gap: 24px;
    font-family: "Lato", sans-serif; font-weight: 700; font-size: 10.5px;
    color: var(--contact-ink);
  }
  .contact-item { display: flex; align-items: center; gap: 5px; }
  .contact-icon { width: 10px; height: 10px; }
  .address-band {
    position: absolute; left: 0; right: 0; bottom: 0; height: 37px;
    background: linear-gradient(90deg, var(--brand-deep), var(--brand-plum));
    color: var(--band-text);
    font-family: "Lato", sans-serif; font-size: 10.5px; line-height: 12px;
    text-align: center; padding-top: 6px;
  }
</style>
</head>
<body>
  <main class="letterhead">
    <header class="masthead">
      <div class="masthead-badge"></div>
      <div class="masthead-text">
        <div class="masthead-the">The</div>
        <div class="masthead-name">Tamsel Foundation Inc</div>
        <div class="masthead-tagline">Opening new doors to learning for young minds</div>
      </div>
    </header>

    <div class="watermark" aria-hidden="true">
      <div class="watermark-name">Tamsel<br>Foundation</div>
    </div>

    <footer>
      <div class="contact-row">
        <span class="contact-item">
          <svg class="contact-icon" viewBox="0 0 24 24"><path fill="currentColor" d="M6.6 10.8a15.1 15.1 0 0 0 6.6 6.6l2.2-2.2c.3-.3.7-.4 1-.2 1.1.4 2.3.6 3.6.6.6 0 1 .4 1 1V20c0 .6-.4 1-1 1C10.6 21 3 13.4 3 4c0-.6.4-1 1-1h3.5c.6 0 1 .4 1 1 0 1.3.2 2.5.6 3.6.1.3 0 .7-.2 1z"/></svg>
          04418-5550-1936
        </span>
        <span class="contact-item">
          <svg class="contact-icon" viewBox="0 0 24 24"><rect x="2" y="5" width="20" height="14" fill="none" stroke="currentColor" stroke-width="2"/><path d="M2 5l10 8 10-8" fill="none" stroke="currentColor" stroke-width="2"/></svg>
          hello@tamselfoundation.example
        </span>
      </div>
      <div class="address-band">
        Suite 4, 118 Example Avenue, New York, USA,<br>
        Copyright 2016
      </div>
    </footer>
  </main>
</body>
</html>
```